Brackenford Hearing Clinic Business Card Design Project

We need a new business card design. We changed our logo recently and need to update our cards. We are a small hearing clinic with a 3 locations in BC. We help people with hearing loss by fitting them with hearing instruments that are appropriate for them and help them overcome the challenges that hearing loss causes. The symbol part of our logo represents the three important components of successful outcome. The three are: 1-acceptance of the change in hearing, 2-a hearing care provider that cares and is knowledgeable and experienced, 3-a quality hearing instrument. I would like to have a clean design that shows quality commitment to a successful end result of treatment. Here is our website for more information. www.earlumo.ca

Target Market(s)

Senior population - mostly 50+

Industry/Entity Type

Clinic

Requirements
Must have
• Logo
Name - Devon Pallister
Title - Hearing Instrument Practitioner (can be very small)
Phone: 250 637-4819
Address: 415-B 22nd Street, Marrowdale, BC V1X 2K7
Email: devon@earlumo.ca
website address: www.earlumo.ca
Nice to have
• Could be both sided and have a photo on the card.

```html
<!DOCTYPE html>
<html lang="en">
<head>
<meta charset="utf-8">
<title>Brackenford Hearing Clinic – Business Card</title>
<link rel="stylesheet" href="https://fonts.googleapis.com/css2?family=Nunito:wght@800&family=Nunito+Sans:wght@300;400&display=swap">
<style>
  :root {
    --page: #e9e7e3;
    --card: #f4f4f3;
    --blue: #1f5aa6;
    --orange: #e08a1e;
    --green: #7ab33e;
    --ink: #2f3236;
    --ink-soft: #4a4d52;
    --photo-warm: #c9701f;
    --photo-mid: #a85418;
    --photo-deep: #5a3a7a;
  }
  * { box-sizing: border-box; margin: 0; padding: 0; }
  html, body { width: 1200px; height: 900px; overflow: hidden; }
  body {
    background: var(--page);
    font-family: "Nunito Sans", Arial, sans-serif;
    position: relative;
  }
  .card {
    position: absolute;
    left: 250px;
    width: 700px;
    height: 400px;
    box-shadow: 0 6px 18px rgba(0,0,0,0.18);
    overflow: hidden;
  }
  .card--back { top: 40px; }
  .card--front { top: 460px; background: var(--card); }

  .team-photo {
    position: absolute; inset: 0;
    background: linear-gradient(115deg, var(--photo-warm) 0%, var(--photo-mid) 45%, var(--photo-deep) 100%);
  }
  .back-brand {
    position: absolute; left: 36px; bottom: 30px;
    display: flex; align-items: center; gap: 10px;
    font-family: "Nunito", Arial, sans-serif; font-weight: 800;
    font-size: 18px; color: #ffffff;
  }
  .back-brand .dot { width: 22px; height: 22px; border-radius: 50%; background: #ffffff; }

  .brand {
    position: absolute; left: 48px; top: 70px;
    display: flex; align-items: center; gap: 14px;
  }
  .brand .dot { width: 56px; height: 56px; border-radius: 50%; background: var(--blue); }
  .brand-name {
    font-family: "Nunito", Arial, sans-serif; font-weight: 800;
    font-size: 38px; line-height: 1; letter-spacing: -0.5px; color: var(--blue);
    white-space: nowrap;
  }
  .person { position: absolute; left: 52px; top: 250px; }
  .person-name {
    font-weight: 300; font-size: 30px; letter-spacing: 2px;
    color: var(--ink); text-transform: uppercase; white-space: nowrap;
  }
  .person-title { font-weight: 400; font-size: 17px; color: var(--ink-soft); margin-top: 4px; }

  .contacts {
    position: absolute; left: 430px; top: 190px;
    list-style: none; display: flex; flex-direction: column; gap: 12px;
  }
  .contacts li {
    display: flex; align-items: flex-start; gap: 10px;
    font-size: 15px; color: var(--ink-soft); line-height: 1.3; white-space: nowrap;
  }
  .icon {
    flex: 0 0 22px; width: 22px; height: 22px; border-radius: 50%;
    display: flex; align-items: center; justify-content: center;
  }
  .icon--orange { background: var(--orange); }
  .icon--green { background: var(--green); }
  .icon--blue { background: var(--blue); }
  .icon svg { width: 12px; height: 12px; }
</style>
</head>
<body>
  <section class="card card--back">
    <div class="team-photo" role="img" aria-label="Portrait photo of the two clinic practitioners standing in a warm orange-toned office"></div>
    <div class="back-brand"><span class="dot"></span>Brackenford Hearing Clinic</div>
  </section>

  <section class="card card--front">
    <div class="brand">
      <span class="dot"></span>
      <span class="brand-name">Brackenford Hearing Clinic</span>
    </div>

    <div class="person">
      <p class="person-name">Devon Pallister</p>
      <p class="person-title">Hearing Instrument Practitioner</p>
    </div>

    <ul class="contacts">
      <li>
        <span class="icon icon--orange"><svg viewBox="0 0 12 12"><path d="M2.5 1 L4.5 1 L5 3.5 L3.8 4.4 C4.4 5.8 5.7 7.3 7.3 8 L8.2 6.9 L10.8 7.4 L10.8 9.5 C10.8 10.3 10 10.9 9.2 10.8 C5.2 10.3 1.6 6.8 1.2 2.7 C1.1 1.8 1.7 1 2.5 1 Z" fill="#fff"/></svg></span>
        250 637-4819
      </li>
      <li>
        <span class="icon icon--green"><svg viewBox="0 0 12 12"><rect x="1" y="2.5" width="10" height="7" fill="none" stroke="#fff" stroke-width="1.2"/><path d="M1 2.5 L6 6.5 L11 2.5" fill="none" stroke="#fff" stroke-width="1.2"/></svg></span>
        devon@earlumo.ca
      </li>
      <li>
        <span class="icon icon--orange"><svg viewBox="0 0 12 12"><circle cx="6" cy="6" r="4.8" fill="none" stroke="#fff" stroke-width="1.1"/><ellipse cx="6" cy="6" rx="2" ry="4.8" fill="none" stroke="#fff" stroke-width="1"/><path d="M1.2 6 H10.8" stroke="#fff" stroke-width="1"/></svg></span>
        www.earlumo.ca
      </li>
      <li>
        <span class="icon icon--blue"><svg viewBox="0 0 12 12"><path d="M6 11 C6 11 2.3 7 2.3 4.7 A3.7 3.7 0 0 1 9.7 4.7 C9.7 7 6 11 6 11 Z" fill="#fff"/><circle cx="6" cy="4.7" r="1.4" fill="#1f5aa6"/></svg></span>
        <span>415-B 22nd Street,<br>Marrowdale, BC V1X 2K7</span>
      </li>
    </ul>
  </section>
</body>
</html>
```